BrightKeel Business Card Contest

We are looking for a modern business card that catches attention and is unique. Attached is the brand guide and logo files. Please note that the back side (not the side with our name and info) with be UV raise printed, so have fun with the design there. We want to include Name, Title, Phone number, email, website.

Contact Information for Business Card

Please see project description

```html
<!DOCTYPE html>
<html lang="en">
<head>
<meta charset="utf-8">
<title>BrightKeel Business Card</title>
<link rel="stylesheet" href="https://fonts.googleapis.com/css2?family=Montserrat:wght@400;500;700;800&display=swap">
<style>
  :root {
    --stage: #e9eaee;
    --card-white: #f4f3f8;
    --card-dark: #1c1c1e;
    --pattern-light: #3a3a3d;
    --pattern-dark: #121213;
    --ink: #1e1f24;
    --royal: #1f4aa8;
    --navy: #223663;
    --silver: #b9c3cb;
    --sky: #2bb3e0;
    --rule: #4b4f7a;
  }
  * { box-sizing: border-box; margin: 0; padding: 0; }
  html, body { width: 1200px; height: 947px; overflow: hidden; }
  body {
    background: var(--stage);
    font-family: "Montserrat", sans-serif;
    position: relative;
  }
  .card {
    position: absolute;
    width: 680px;
    height: 388px;
    border-radius: 22px;
    overflow: hidden;
    box-shadow: 0 14px 34px rgba(0,0,0,0.18);
  }
  /* Back side */
  .card-back {
    left: 70px;
    top: 50px;
    background: var(--card-dark);
  }
  .card-back .uv-pattern {
    position: absolute;
    inset: 0;
    background: linear-gradient(120deg, var(--pattern-dark) 0%, var(--card-dark) 45%, var(--pattern-light) 100%);
  }
  .card-back .wordmark {
    position: absolute;
    left: 50%;
    top: 50%;
    transform: translate(-50%, -50%);
    display: flex;
    align-items: center;
    gap: 16px;
    color: #ffffff;
  }
  /* Front side */
  .card-front {
    left: 450px;
    top: 508px;
    background: var(--card-white);
  }
  .card-front .swoosh {
    position: absolute;
    inset: 0;
  }
  .card-front .wordmark {
    position: absolute;
    left: 52px;
    top: 148px;
    display: flex;
    align-items: center;
    gap: 14px;
    color: var(--ink);
  }
  .wordmark-mark {
    width: 30px;
    height: 30px;
    background: var(--sky);
  }
  .wordmark-name {
    font-weight: 500;
    font-size: 46px;
    letter-spacing: -0.5px;
  }
  .divider {
    position: absolute;
    left: 352px;
    top: 96px;
    width: 1.5px;
    height: 150px;
    background: var(--rule);
  }
  .contact-block {
    position: absolute;
    left: 378px;
    top: 88px;
  }
  .person-name {
    font-weight: 800;
    font-size: 25px;
    color: var(--royal);
    letter-spacing: 0.4px;
    text-transform: uppercase;
  }
  .person-title {
    font-size: 15px;
    color: var(--ink);
    margin-top: 2px;
  }
  .contact-list {
    list-style: none;
    margin-top: 18px;
  }
  .contact-list li {
    display: flex;
    align-items: center;
    gap: 10px;
    font-size: 15px;
    color: var(--ink);
    line-height: 26px;
  }
  .contact-list svg { width: 14px; height: 14px; flex: none; }
</style>
</head>
<body>
  <section class="card card-back" aria-label="Card back">
    <div class="uv-pattern" role="img" aria-label="Raised UV gloss pattern of repeated geometric shapes on black"></div>
    <div class="wordmark">
      <span class="wordmark-mark" aria-hidden="true"></span>
      <span class="wordmark-name">BrightKeel</span>
    </div>
  </section>

  <section class="card card-front" aria-label="Card front">
    <svg class="swoosh" viewBox="0 0 680 388" preserveAspectRatio="none" aria-hidden="true">
      <path d="M250 388 C 420 330, 560 240, 680 120 L680 388 Z" fill="var(--silver)"/>
      <path d="M300 388 C 440 330, 580 220, 680 100 L680 140 C 600 250, 490 330, 380 388 Z" fill="var(--silver)"/>
      <path d="M330 388 C 470 320, 600 210, 680 128 L680 388 Z" fill="var(--navy)"/>
    </svg>

    <div class="wordmark">
      <span class="wordmark-mark" aria-hidden="true"></span>
      <span class="wordmark-name">BrightKeel</span>
    </div>

    <div class="divider"></div>

    <div class="contact-block">
      <h1 class="person-name">Dana Whitfield</h1>
      <p class="person-title">CEO/Director</p>
      <ul class="contact-list">
        <li>
          <svg viewBox="0 0 16 16"><path d="M4 1.5 L6.5 4.5 L5 6.3 C6 8.4 7.6 10 9.7 11 L11.5 9.5 L14.5 12 L13 14.5 C7 14 2 9 1.5 3 Z" fill="var(--sky)"/></svg>
          555-201-4800
        </li>
        <li>
          <svg viewBox="0 0 16 16"><rect x="1" y="3" width="14" height="10" fill="var(--sky)"/><path d="M1 3 L8 9 L15 3" fill="none" stroke="#ffffff" stroke-width="1.3"/></svg>
          info@brightkeel.com
        </li>
        <li>
          <svg viewBox="0 0 16 16"><circle cx="8" cy="8" r="6.5" fill="none" stroke="var(--sky)" stroke-width="1.5"/><ellipse cx="8" cy="8" rx="2.8" ry="6.5" fill="none" stroke="var(--sky)" stroke-width="1.2"/><path d="M1.5 8 H14.5" stroke="var(--sky)" stroke-width="1.2"/></svg>
          brightkeel.com
        </li>
      </ul>
    </div>
  </section>
</body>
</html>
```